Tech Enablement - Trifold

I need at trifold for marketing outreach /collateral for our technology enablement as a service offering.
Details provided in attached doc.

```html
<!DOCTYPE html>
<html lang="en">
<head>
<meta charset="utf-8">
<title>Technology Enablement Trifold</title>
<link href="https://fonts.googleapis.com/css2?family=Poppins:wght@400;500;600;700&display=swap" rel="stylesheet">
<style>
:root{
  --blue:#1479b8;
  --blue-bright:#1fa9d6;
  --blue-deep:#0f5e9c;
  --ice:#c9d9e3;
  --charcoal:#3a3d40;
  --ink:#2d2f31;
  --paper:#e6e6e6;
  --paper-light:#efefef;
  --page:#ffffff;
  --orange:#d9691e;
}
*{margin:0;padding:0;box-sizing:border-box}
html,body{width:1200px;height:954px;overflow:hidden;background:var(--page)}
body{font-family:"Poppins",sans-serif;color:var(--ink);position:relative}
.sheet{position:absolute;left:270px;width:660px;height:440px;display:flex;box-shadow:0 10px 30px rgba(0,0,0,.18)}
.sheet--inside{top:22px}
.sheet--outside{top:492px}
.panel{position:relative;width:220px;height:440px;overflow:hidden;background:linear-gradient(160deg,var(--paper-light),var(--paper))}
.panel + .panel{border-left:1px solid rgba(0,0,0,.06)}
.deco{position:absolute;left:0;top:0;width:220px;height:440px}
.photo{position:absolute}
.shield-badge{position:absolute;width:30px;height:34px}
h2{font-weight:700;color:var(--blue);font-size:14px;line-height:1.1;position:absolute}
p,li{font-size:7px;line-height:1.45}
.block{position:absolute}
ul{list-style:none}
ul li::before{content:"• "}
.label{font-weight:700;font-size:7px;margin-top:5px}
.problem-grid{position:absolute;left:18px;top:118px;width:190px;display:grid;grid-template-columns:1fr 1fr;gap:10px 8px}
.problem-item{display:flex;gap:5px;align-items:flex-start;font-size:6.5px;line-height:1.35}
.problem-item svg{flex:0 0 13px;height:15px}
.brand{display:flex;align-items:center;gap:5px;font-weight:600;letter-spacing:1.5px;text-transform:uppercase}
.brand-dot{width:9px;height:9px;border-radius:50%;background:currentColor}
.cover-text{position:absolute;left:20px;top:120px;width:190px;display:flex;flex-direction:column;gap:6px}
.cover-title{color:#fff;font-weight:600;font-size:14px;line-height:1.2}
.cover-sub{color:#f2f2f2;font-size:7px;line-height:1.4}
.cta{position:absolute;left:16px;top:298px;font-weight:700;color:var(--blue);font-size:10.5px;line-height:1.15}
.cta-link{position:absolute;left:16px;top:342px;font-size:7px;text-decoration:underline;font-weight:500;width:90px;line-height:1.35}
</style>
</head>
<body>

<!-- Inside spread -->
<section class="sheet sheet--inside">
  <!-- Problem panel -->
  <article class="panel">
    <svg class="shield-badge" style="left:18px;top:18px" viewBox="0 0 30 34"><path d="M15 1 L28 6 V16 C28 25 22 30 15 33 C8 30 2 25 2 16 V6 Z" fill="var(--blue)"/></svg>
    <h2 style="left:18px;top:62px;width:190px">The Problem We Solve</h2>
    <p class="block" style="left:18px;top:82px;width:190px">Most businesses don't have a technology problem. They have an enablement problem.</p>
    <div class="problem-grid">
      <div class="problem-item"><svg viewBox="0 0 13 15"><path d="M6.5 0 L13 2.5 V7 C13 11 10 13.5 6.5 15 C3 13.5 0 11 0 7 V2.5 Z" fill="var(--charcoal)"/></svg><span>Plenty of software, no real system</span></div>
      <div class="problem-item"><svg viewBox="0 0 13 15"><path d="M6.5 0 L13 2.5 V7 C13 11 10 13.5 6.5 15 C3 13.5 0 11 0 7 V2.5 Z" fill="var(--charcoal)"/></svg><span>Manual work filling the gaps</span></div>
      <div class="problem-item"><svg viewBox="0 0 13 15"><path d="M6.5 0 L13 2.5 V7 C13 11 10 13.5 6.5 15 C3 13.5 0 11 0 7 V2.5 Z" fill="var(--charcoal)"/></svg><span>Processes living in people's heads</span></div>
      <div class="problem-item"><svg viewBox="0 0 13 15"><path d="M6.5 0 L13 2.5 V7 C13 11 10 13.5 6.5 15 C3 13.5 0 11 0 7 V2.5 Z" fill="var(--charcoal)"/></svg><span>Poor adoption of tools already paid for</span></div>
      <div class="problem-item"><svg viewBox="0 0 13 15"><path d="M6.5 0 L13 2.5 V7 C13 11 10 13.5 6.5 15 C3 13.5 0 11 0 7 V2.5 Z" fill="var(--charcoal)"/></svg><span>Limited visibility into performance</span></div>
      <div class="problem-item"><svg viewBox="0 0 13 15"><path d="M6.5 0 L13 2.5 V7 C13 11 10 13.5 6.5 15 C3 13.5 0 11 0 7 V2.5 Z" fill="var(--charcoal)"/></svg><span>Reactive technology decisions</span></div>
    </div>
    <p class="block" style="left:18px;top:205px;width:190px">The result: More effort, more admin, less return on software spend.</p>
    <div class="photo" role="img" aria-label="Photo of a team meeting around a wooden table with laptops and notes" style="left:0;top:250px;width:220px;height:150px;clip-path:polygon(0 22%,100% 0,100% 62%,60% 100%,0 78%);background:linear-gradient(135deg,#6b4a32,#a37a55 45%,#d8c9b4 75%,#8a6a4e)"></div>
    <svg class="deco" viewBox="0 0 220 440" aria-hidden="true">
      <polygon points="60,400 220,340 220,440 140,440" fill="var(--blue-bright)"/>
      <polygon points="60,400 140,440 90,440" fill="var(--blue-deep)"/>
      <polygon points="130,380 220,340 220,400" fill="var(--ice)" opacity=".7"/>
    </svg>
  </article>

  <!-- Approach panel -->
  <article class="panel">
    <svg class="deco" viewBox="0 0 220 440" aria-hidden="true">
      <polygon points="70,440 110,410 150,440" fill="var(--charcoal)"/>
    </svg>
    <h2 style="left:18px;top:48px;width:190px">Our Approach: Technology Enablement</h2>
    <div class="block" style="left:18px;top:86px;width:190px">
      <p>Technology Enablement improves how work flows through your business:</p>
      <ul><li>Workflows before tools</li><li>Adoption before automation</li><li>Outcomes before technology decisions</li></ul>
      <p class="label">What makes us different:</p>
      <ul><li>No requirement to replace systems</li><li>No need to change IT providers</li><li>No long-term contracts</li><li>Clarity first, execution only where it makes sense</li></ul>
    </div>
    <div class="photo" role="img" aria-label="Line illustration of a person working on a laptop beside floating web interface windows" style="left:30px;top:235px;width:160px;height:140px;border-radius:50%;background:radial-gradient(circle,#e9f1f7 0%,#d6e4ee 60%,transparent 72%)"></div>
  </article>

  <!-- Assessment panel -->
  <article class="panel">
    <svg class="deco" viewBox="0 0 220 440" aria-hidden="true">
      <polygon points="0,150 40,60 60,150 30,190" fill="var(--orange)"/>
    </svg>
    <div class="photo" role="img" aria-label="Photo of a smiling businesswoman at a laptop in a bright office" style="left:20px;top:20px;width:200px;height:160px;clip-path:polygon(15% 0,100% 0,100% 20%,35% 100%,0 100%,0 35%);background:linear-gradient(140deg,#4a6a7a,#9aa9ae 40%,#c9b9a8 60%,#5a6a55)"></div>
    <h2 style="left:18px;top:200px;width:195px">Technology Enablement Assessment</h2>
    <div class="block" style="left:18px;top:236px;width:195px">
      <p>Start with clarity.</p>
      <ul><li>2–4 week, stand-alone assessment</li><li>Fixed scope, fixed price</li><li>Low risk, high insight</li></ul>
      <p class="label">What we assess:</p>
      <ul><li>Workflows and handoffs</li><li>Technology and digital maturity</li><li>Adoption and training gaps</li><li>Automation and integration opportunities</li><li>Data, reporting, and KPI visibility</li></ul>
      <p class="label">What you receive:</p>
      <ul><li>A prioritized Improvement Roadmap</li><li>Clear business impact and effort</li><li>Confidence before spending more money</li></ul>
    </div>
  </article>
</section>

<!-- Outside spread -->
<section class="sheet sheet--outside">
  <!-- Service panel -->
  <article class="panel">
    <svg class="shield-badge" style="left:18px;top:18px" viewBox="0 0 30 34"><path d="M15 1 L28 6 V16 C28 25 22 30 15 33 C8 30 2 25 2 16 V6 Z" fill="var(--blue)"/></svg>
    <h2 style="left:18px;top:62px;width:190px">Technology Enablement as a Service</h2>
    <div class="block" style="left:18px;top:98px;width:190px">
      <p>Turn clarity into action — at your pace.</p>
      <ul><li>Ongoing enablement support</li><li>No per-seat pricing</li><li>No traditional IT contract</li></ul>
      <p class="label">What it includes:</p>
      <ul><li>Strategic technology oversight</li><li>Living roadmap management</li><li>Workflow and process improvement</li><li>Adoption and change support</li><li>Vendor and tool coordination</li><li>Execution guidance across tools, data, and automation</li></ul>
    </div>
    <div class="photo" role="img" aria-label="Photo of a woman using a tablet surrounded by glowing digital interface graphics" style="left:80px;top:290px;width:140px;height:150px;clip-path:polygon(0 10%,100% 0,100% 65%,55% 100%,0 100%);background:linear-gradient(150deg,#1d3c5c,#3f7fa8 40%,#d4963e 70%,#2a4f6e)"></div>
    <svg class="deco" viewBox="0 0 220 440" aria-hidden="true">
      <polygon points="0,300 40,260 90,330 0,330" fill="var(--blue-bright)"/>
      <polygon points="0,330 90,330 60,440 0,440" fill="var(--ice)"/>
      <polygon points="60,300 90,330 70,340" fill="var(--blue)"/>
    </svg>
  </article>

  <!-- Back panel -->
  <article class="panel">
    <svg class="deco" viewBox="0 0 220 440" aria-hidden="true">
      <polygon points="0,0 60,0 30,50" fill="var(--charcoal)"/>
      <polygon points="120,0 220,0 220,80 190,110" fill="var(--blue-deep)"/>
      <polygon points="200,0 220,0 220,30" fill="var(--charcoal)"/>
      <polygon points="160,300 220,270 220,390" fill="var(--blue-bright)" opacity=".35"/>
    </svg>
    <div class="brand block" style="left:80px;top:78px;color:var(--blue);font-size:13px"><span class="brand-dot"></span>Veltora</div>
    <h2 style="left:16px;top:112px;width:195px">Execution &amp; Managed IT</h2>
    <div class="block" style="left:16px;top:132px;width:195px">
      <p>When execution and trust are established, deeper partnership follows.</p>
      <ul><li>Confident execution</li><li>Deeper technical ownership</li><li>Managed IT and infrastructure support</li></ul>
      <p class="label">Why this comes last:</p>
      <ul><li>Clients already trust the roadmap</li><li>Veltora understands the business</li><li>Decisions are informed, not reactive</li></ul>
    </div>
    <p class="cta">Start with clarity.<br>Build with confidence.<br>Scale with control.</p>
    <p class="cta-link">Book a Technology Enablement Assessment</p>
    <div class="photo" role="img" aria-label="Line illustration of a person with a laptop beside a floating web browser window" style="left:128px;top:338px;width:82px;height:46px;border-radius:8px;background:linear-gradient(150deg,#dbe8f1,#c6dbea)"></div>
    <p class="block" style="left:16px;top:392px;width:195px">Wherever you are in your technology journey, Veltora meets you there — and helps you move forward with purpose.</p>
  </article>

  <!-- Cover panel -->
  <article class="panel">
    <div class="photo" role="img" aria-label="Photo of a businessman with glasses drinking coffee at a laptop beside a potted plant" style="left:0;top:0;width:220px;height:440px;background:linear-gradient(170deg,#8f8678 0%,#7d7a73 35%,#4f5a52 60%,#2e3438 80%,#5a6670 100%)"></div>
    <svg class="deco" viewBox="0 0 220 440" aria-hidden="true">
      <polygon points="0,0 120,0 60,50 0,40" fill="var(--blue-bright)"/>
      <polygon points="0,0 40,0 0,30" fill="var(--charcoal)"/>
      <polygon points="60,50 120,0 200,20 90,80" fill="var(--ice)" opacity=".85"/>
      <polygon points="120,0 220,0 220,40" fill="var(--blue)"/>
      <rect x="150" y="60" width="34" height="28" fill="none" stroke="var(--blue)" stroke-width="3"/>
      <polygon points="0,400 220,300 220,440 0,440" fill="var(--blue)"/>
      <polygon points="80,440 220,360 220,440" fill="var(--blue-bright)"/>
      <polygon points="0,400 100,355 60,440 0,440" fill="var(--blue-deep)" opacity=".7"/>
    </svg>
    <div class="cover-text">
      <p class="cover-title">Technology Enablement for Growing Businesses</p>
      <p class="cover-sub">Turn disconnected tools into systems that actually work. Clarity before complexity. Enablement before IT.</p>
    </div>
    <div class="brand block" style="left:140px;top:410px;color:#fff;font-size:10px"><span class="brand-dot"></span>Veltora</div>
  </article>
</section>

</body>
</html>
```